a little bit like bulkhop but selling small amounts of high end tech gear directly to customers inbox.

Hi Designers,

I have had my artflock logo attached to this project.
I have another web site (coolriver.com.au)which will be dedicated mostly to
enthusiast,s that want to water cool their pc's. It's not quite finished. I may
need your help with that one once we get Gizminibox up and running .I
like Rig Shell Depot layout for Coolriver
I want Gizmini to be simple to navigate, and similar to Bulkhop.
I will be selling Enthusiast PC Components in small volumes ie first in
best dressed. weekly specials,daily specials,free shipping
There should be the ability for me to upload the component photo direct
from my Orbit5 Phone .
Links to the manufacturers website and product reviews from vidstream
I will give you more in depth details tomorrow.

I would like my new site to be similar to e-Gadj.com.au but cooler! Added Sunday, October 1, 2017

Target Market(s)

Enthusiast PC Builders

Industry/Entity Type

Tech

Coding

Coded - Design and coding required

Number of Pages Required

1 page

Font styles to use
Sans Serif

Colors
33b8a4

Requirements
Must have
• Link the price of my product to pricora.com.au
• Drop down menus

```html
<!DOCTYPE html>
<html lang="en">
<head>
<meta charset="utf-8">
<title>Gizminibox – Enthusiast PC Components</title>
<link href="https://fonts.googleapis.com/css2?family=Roboto:wght@400;500;700&family=Roboto+Condensed:wght@700&display=swap" rel="stylesheet">
<style>
:root{
  --teal:#33b8a4;
  --teal-dark:#2a9c8b;
  --ink:#333;
  --muted:#777;
  --line:#e3e3e3;
  --soft:#f4f4f4;
  --red:#e21b1b;
  --orange:#f26b1d;
  --dark:#2b2b2b;
  --shot-a:#2a1f4a;
  --shot-b:#8a74c8;
}
*{box-sizing:border-box;margin:0;padding:0}
html,body{width:1200px;height:4500px;overflow:hidden;background:#fff}
body{font-family:"Roboto",Arial,sans-serif;color:var(--ink);font-size:14px;position:relative}
.abs{position:absolute}
a{color:inherit;text-decoration:none}

/* top strip */
.topbar{top:0;left:0;width:1200px;height:24px;background:var(--soft);border-bottom:1px solid var(--line);font-size:12px;color:var(--muted)}
.topbar .welcome{position:absolute;left:96px;top:5px}
.topbar .account{position:absolute;right:90px;top:5px;display:flex;gap:22px}
.topbar .account span::before{content:"";display:inline-block;width:7px;height:7px;border-radius:50%;background:var(--teal);margin-right:6px}

/* header */
.brand{left:96px;top:48px;display:flex;align-items:center;gap:12px}
.brand .mark{width:40px;height:40px;background:var(--teal)}
.brand .name{font-size:40px;font-weight:700;color:#1d4e73;letter-spacing:-1px}
.search{left:360px;top:60px;width:495px;height:45px;display:flex}
.search .field{flex:1;border:2px solid var(--teal);border-right:0;padding:12px;font-size:13px;color:#aaa}
.search .btn{width:96px;background:var(--teal);color:#fff;font-weight:700;font-size:13px;display:flex;align-items:center;justify-content:center}
.hotline{left:880px;top:60px;display:flex;gap:12px;align-items:center}
.hotline .txt{font-size:13px;color:var(--muted);line-height:20px}
.hotline .txt b{color:var(--red);font-size:19px;font-weight:700}

/* nav */
.nav{top:198px;left:0;width:1200px;height:48px;background:var(--teal)}
.nav ul{list-style:none;display:flex;position:absolute;left:96px;top:0;height:48px;align-items:center;gap:40px;color:#fff;font-size:14px}
.nav .cart{position:absolute;left:990px;top:0;width:120px;height:48px;background:var(--dark);color:#fff;font-size:11px;display:flex;align-items:center;gap:8px;padding-left:14px;line-height:14px}

.hero{top:264px;left:96px;width:1014px;height:351px;background:radial-gradient(circle at 30% 40%,#5aa5ff 0,#1a3c7a 30%,#0c1120 70%),#111}

/* categories */
.cats{top:645px;left:96px;width:234px;height:420px;border:1px solid var(--line)}
.cats h3{background:var(--teal);color:#fff;font-size:13px;font-weight:700;height:45px;line-height:45px;padding-left:16px}
.cats li{list-style:none;height:45px;line-height:44px;border-bottom:1px solid var(--line);padding-left:24px;font-size:13px;position:relative;background:var(--soft)}
.cats li::after{content:"›";position:absolute;right:16px;color:#999}
.cats li.promo{background:#fff}
.cats li.promo::before{content:"";position:absolute;left:8px;top:16px;width:12px;height:12px;background:var(--red);border-radius:3px}
.cats li.more::after{content:none}

/* section frame */
.block{border:1px solid var(--line);background:#fff}
.block-head{height:45px;background:var(--soft);border-bottom:1px solid var(--line);position:relative;display:flex;align-items:center;padding-left:15px;gap:24px}
.block-head h2{font-size:14px;font-weight:700;text-transform:uppercase;height:45px;line-height:45px;border-bottom:3px solid var(--teal)}
.block-head .tabs{font-size:12px;color:var(--muted)}
.block-head .arrows{position:absolute;right:14px;top:14px;font-size:16px;color:#555;letter-spacing:8px}
.shot{background:linear-gradient(160deg,var(--shot-a),var(--shot-b) 55%,#1b1530)}

/* selling */
.selling{top:645px;left:339px;width:771px;height:420px}
.sell-grid{display:grid;grid-template-columns:1fr 1fr;padding:0 20px}
.sell-item{display:flex;gap:20px;padding:26px 0;height:187px;border-bottom:1px solid var(--line)}
.sell-item:nth-child(n+3){border-bottom:0}
.sell-item .shot{width:78px;height:126px;flex:none}
.sell-item p{font-size:12px;line-height:17px;width:200px}
.price{color:var(--red);font-weight:700;font-size:13px;margin-top:6px}
.old{color:#999;text-decoration:line-through;font-size:12px;margin-top:6px}
.off{display:inline-block;background:#3db24b;color:#fff;font-size:10px;padding:1px 4px;margin-left:6px}
.buy{display:inline-block;margin-top:14px;border:1px solid var(--teal);color:var(--teal);font-size:10px;padding:6px 12px}

/* product rows */
.products{left:96px;width:1014px;height:420px}
.row{display:flex;gap:24px;padding:15px 15px 0}
.card{width:144px}
.card .shot{height:210px}
.card p{font-size:12px;line-height:16px;margin-top:10px}
.card .price{margin-top:4px}
.see-more{position:absolute;left:0;bottom:0;width:100%;height:30px;background:var(--soft);border-top:1px solid var(--line);text-align:center;line-height:30px;font-size:12px;color:#555}

/* news */
.news-head{top:3381px;left:96px;width:1014px;height:40px;border-bottom:1px solid var(--line)}
.news-head h2{font-size:14px;font-weight:700;display:inline-block;height:40px;border-bottom:3px solid var(--teal)}
.news{top:3435px;left:96px;width:1014px;display:flex;gap:24px}
.post{width:322px}
.post .shot{height:420px}
.post h4{font-size:13px;font-weight:700;margin-top:18px;line-height:18px}
.post time{display:block;font-size:11px;color:#999;margin-top:4px}
.post p{font-size:12px;color:var(--muted);margin-top:6px;line-height:17px}

/* services */
.services{top:4134px;left:0;width:1200px;height:72px;background:var(--soft);border-top:1px solid var(--line);border-bottom:1px solid var(--line)}
.services ul{list-style:none;display:flex;position:absolute;left:96px;top:14px;width:1014px}
.services li{flex:1;display:flex;gap:12px}
.services b{display:block;font-size:11px;font-weight:700}
.services span{font-size:10px;color:var(--muted);line-height:13px}

/* footer */
.footer{top:4230px;left:96px;width:1014px;display:flex}
.footer section{flex:1}
.footer h5{font-size:12px;font-weight:700;text-transform:uppercase;padding-bottom:10px;border-bottom:1px solid var(--line);margin-bottom:12px;width:220px}
.footer li{list-style:none;font-size:12px;color:#555;line-height:30px}
.footer li::before{content:"› ";color:#999}
.footer .contact li{line-height:18px;margin-bottom:10px;display:flex;gap:8px}
.footer .contact li::before{content:none}
.footer .contact i{flex:none;width:14px;height:14px;background:var(--orange);border-radius:50%;margin-top:2px}
.bottom{top:4464px;left:0;width:1200px;height:36px;background:var(--dark);color:#aaa;font-size:11px;text-align:center;line-height:36px}
.bottom b{color:var(--teal)}
</style>
</head>
<body>

<div class="abs topbar"><span class="welcome">Welcome to Gizminibox</span><div class="account"><span>Log in</span><span>Account</span></div></div>

<div class="abs brand"><div class="mark"></div><div class="name">gizminibox</div></div>
<div class="abs search"><div class="field">Search</div><div class="btn">SEARCH</div></div>
<div class="abs hotline">
  <svg width="42" height="42" viewBox="0 0 42 42"><circle cx="21" cy="21" r="20" fill="#fff" stroke="#e21b1b" stroke-width="3"/><path d="M13 23a8 8 0 0 1 16 0" fill="none" stroke="#e21b1b" stroke-width="3"/><rect x="11" y="22" width="5" height="8" rx="2" fill="#e21b1b"/><rect x="26" y="22" width="5" height="8" rx="2" fill="#e21b1b"/></svg>
  <div class="txt">Hotline: <b>1900 628 310</b><br>Email: support@gizminibox.com</div>
</div>

<nav class="abs nav">
  <ul><li>Home page</li><li>Introduce</li><li>Product Categories ▾</li><li>News</li><li>Recruitment</li><li>Contact</li></ul>
  <div class="cart"><svg width="22" height="20" viewBox="0 0 22 20"><path d="M1 2h4l3 11h10l3-8H7" fill="none" stroke="#fff" stroke-width="2"/><circle cx="9" cy="17" r="2" fill="#fff"/><circle cx="17" cy="17" r="2" fill="#fff"/></svg><span>CART<br>0 products</span></div>
</nav>

<div class="abs hero" role="img" aria-label="Photo of a water-cooled gaming PC interior with blue-lit fans"></div>

<aside class="abs cats">
  <h3>☰ PRODUCT CATEGORIES</h3>
  <ul><li class="promo">Promotion</li><li>Product</li><li>Product</li><li>Product</li><li>Product</li><li>Product</li><li>Product</li><li class="more">☰ see more</li></ul>
</aside>

<section class="abs block selling">
  <div class="block-head"><h2>Selling products</h2><span class="arrows">‹›</span></div>
  <div class="sell-grid">
    <div class="sell-item"><div class="shot" role="img" aria-label="Custom gaming PC tower"></div><div><p>Custom-built Gaming PC with 32GB RAM and liquid Corvane cooler C8 Winstar 10</p><div class="price">$ 1,234</div><span class="buy">PURCHASE</span></div></div>
    <div class="sell-item"><div class="shot" role="img" aria-label="Custom gaming PC tower"></div><div><p>Custom-built Gaming PC with 32GB RAM and liquid Corvane cooler C8 Winstar 10</p><div class="price">$ 1,234</div><span class="buy">PURCHASE</span></div></div>
    <div class="sell-item"><div class="shot" role="img" aria-label="Custom gaming PC tower"></div><div><p>Custom-built Gaming PC with 32GB RAM and liquid Corvane cooler C8 Winstar 10</p><div class="old">$ 2,345.00<span class="off">-5%</span></div><div class="price">$ 499.00</div><span class="buy">PURCHASE</span></div></div>
    <div class="sell-item"><div class="shot" role="img" aria-label="Custom gaming PC tower"></div><div><p>Custom-built Gaming PC with 32GB RAM and liquid Corvane cooler C8 Winstar 10</p><div class="old">$ 2,345.00<span class="off">-5%</span></div><div class="price">$ 499.00</div><span class="buy">PURCHASE</span></div></div>
  </div>
</section>

<section class="abs block products" style="top:1095px">
  <div class="block-head"><h2>Product highlights</h2><span class="tabs">Products 1 | Products 2 | Products 3 | Products 4</span><span class="arrows">‹›</span></div>
  <div class="row">
    <div class="card"><div class="shot" role="img" aria-label="Gaming PC tower"></div><p>Custom-built Gaming PC with 32GB RAM and</p><div class="price">$ 1,234</div></div>
    <div class="card"><div class="shot" role="img" aria-label="Gaming PC tower"></div><p>Custom-built Gaming PC with 32GB RAM and</p><div class="price">$ 1,234</div></div>
    <div class="card"><div class="shot" role="img" aria-label="Gaming PC tower"></div><p>Custom-built Gaming PC with 32GB RAM and</p><div class="price">$ 1,234</div></div>
    <div class="card"><div class="shot" role="img" aria-label="Gaming PC tower"></div><p>Custom-built Gaming PC with 32GB RAM and</p><div class="price">$ 1,234</div></div>
    <div class="card"><div class="shot" role="img" aria-label="Gaming PC tower"></div><p>Custom-built Gaming PC with 32GB RAM and</p><div class="price">$ 1,234</div></div>
    <div class="card"><div class="shot" role="img" aria-label="Gaming PC tower"></div><p>Custom-built Gaming PC with 32GB RAM and</p><div class="price">$ 1,234</div></div>
  </div>
  <div class="see-more">Xem thêm</div>
</section>

<section class="abs block products" style="top:1551px">
  <div class="block-head"><h2>Products 1</h2><span class="arrows">‹›</span></div>
  <div class="row">
    <div class="card"><div class="shot" role="img" aria-label="Gaming PC tower"></div><p>Custom-built Gaming PC with 32GB RAM and</p><div class="price">$ 1,234</div></div>
    <div class="card"><div class="shot" role="img" aria-label="Gaming PC tower"></div><p>Custom-built Gaming PC with 32GB RAM and</p><div class="price">$ 1,234</div></div>
    <div class="card"><div class="shot" role="img" aria-label="Gaming PC tower"></div><p>Custom-built Gaming PC with 32GB RAM and</p><div class="price">$ 1,234</div></div>
    <div class="card"><div class="shot" role="img" aria-label="Gaming PC tower"></div><p>Custom-built Gaming PC with 32GB RAM and</p><div class="price">$ 1,234</div></div>
    <div class="card"><div class="shot" role="img" aria-label="Gaming PC tower"></div><p>Custom-built Gaming PC with 32GB RAM and</p><div class="price">$ 1,234</div></div>
    <div class="card"><div class="shot" role="img" aria-label="Gaming PC tower"></div><p>Custom-built Gaming PC with 32GB RAM and</p><div class="price">$ 1,234</div></div>
  </div>
  <div class="see-more">see more</div>
</section>

<section class="abs block products" style="top:2010px">
  <div class="block-head"><h2>Products 2</h2><span class="arrows">‹›</span></div>
  <div class="row">
    <div class="card"><div class="shot" role="img" aria-label="Gaming PC tower"></div><p>Custom-built Gaming PC with 32GB RAM and</p><div class="price">$ 1,234</div></div>
    <div class="card"><div class="shot" role="img" aria-label="Gaming PC tower"></div><p>Custom-built Gaming PC with 32GB RAM and</p><div class="price">$ 1,234</div></div>
    <div class="card"><div class="shot" role="img" aria-label="Gaming PC tower"></div><p>Custom-built Gaming PC with 32GB RAM and</p><div class="price">$ 1,234</div></div>
    <div class="card"><div class="shot" role="img" aria-label="Gaming PC tower"></div><p>Custom-built Gaming PC with 32GB RAM and</p><div class="price">$ 1,234</div></div>
    <div class="card"><div class="shot" role="img" aria-label="Gaming PC tower"></div><p>Custom-built Gaming PC with 32GB RAM and</p><div class="price">$ 1,234</div></div>
    <div class="card"><div class="shot" role="img" aria-label="Gaming PC tower"></div><p>Custom-built Gaming PC with 32GB RAM and</p><div class="price">$ 1,234</div></div>
  </div>
  <div class="see-more">see more</div>
</section>

<section class="abs block products" style="top:2466px">
  <div class="block-head"><h2>Products 3</h2><span class="arrows">‹›</span></div>
  <div class="row">
    <div class="card"><div class="shot" role="img" aria-label="Gaming PC tower"></div><p>Custom-built Gaming PC with 32GB RAM and</p><div class="price">$ 1,234</div></div>
    <div class="card"><div class="shot" role="img" aria-label="Gaming PC tower"></div><p>Custom-built Gaming PC with 32GB RAM and</p><div class="price">$ 1,234</div></div>
    <div class="card"><div class="shot" role="img" aria-label="Gaming PC tower"></div><p>Custom-built Gaming PC with 32GB RAM and</p><div class="price">$ 1,234</div></div>
    <div class="card"><div class="shot" role="img" aria-label="Gaming PC tower"></div><p>Custom-built Gaming PC with 32GB RAM and</p><div class="price">$ 1,234</div></div>
    <div class="card"><div class="shot" role="img" aria-label="Gaming PC tower"></div><p>Custom-built Gaming PC with 32GB RAM and</p><div class="price">$ 1,234</div></div>
    <div class="card"><div class="shot" role="img" aria-label="Gaming PC tower"></div><p>Custom-built Gaming PC with 32GB RAM and</p><div class="price">$ 1,234</div></div>
  </div>
  <div class="see-more">see more</div>
</section>

<section class="abs block products" style="top:2922px">
  <div class="block-head"><h2>Products 4</h2><span class="arrows">‹›</span></div>
  <div class="row">
    <div class="card"><div class="shot" role="img" aria-label="Gaming PC tower"></div><p>Custom-built Gaming PC with 32GB RAM and</p><div class="price">$ 1,234</div></div>
    <div class="card"><div class="shot" role="img" aria-label="Gaming PC tower"></div><p>Custom-built Gaming PC with 32GB RAM and</p><div class="price">$ 1,234</div></div>
    <div class="card"><div class="shot" role="img" aria-label="Gaming PC tower"></div><p>Custom-built Gaming PC with 32GB RAM and</p><div class="price">$ 1,234</div></div>
    <div class="card"><div class="shot" role="img" aria-label="Gaming PC tower"></div><p>Custom-built Gaming PC with 32GB RAM and</p><div class="price">$ 1,234</div></div>
    <div class="card"><div class="shot" role="img" aria-label="Gaming PC tower"></div><p>Custom-built Gaming PC with 32GB RAM and</p><div class="price">$ 1,234</div></div>
    <div class="card"><div class="shot" role="img" aria-label="Gaming PC tower"></div><p>Custom-built Gaming PC with 32GB RAM and</p><div class="price">$ 1,234</div></div>
  </div>
  <div class="see-more">see more</div>
</section>

<div class="abs news-head"><h2>NEWS</h2></div>
<div class="abs news">
  <article class="post"><div class="shot" role="img" aria-label="Gaming PC tower with purple lighting"></div><h4>POMELO FIRST DIRECT SELLING PAID UPHONE WARRANTY</h4><time>Monday, 14/11/2016 09:16</time><p>Previously, people could easily buy samples like the Pomelo phone as a refurbished unit on the online store for less.</p></article>
  <article class="post"><div class="shot" role="img" aria-label="Gaming PC tower with purple lighting"></div><h4>UPHONE 7 JET BLACK AND KAZUMI MIX: WHO WILL WIN THE TITLE "THE DIRTIEST PLANT"?</h4><time>Monday, 14/11/2016 09:16</time><p>Both machines have a flashy appearance, shiny and cool, but we wonder which is the dirtiest in terms of design.</p></article>
  <article class="post"><div class="shot" role="img" aria-label="Gaming PC tower with purple lighting"></div><h4>WAY TO BACK UP YOUR MESSAGES AND SIMPLY CALL ON ROBOTIX</h4><time>Sunday, 13/11/2016 09:16</time><p>Sometimes, in the course of using a smartphone, you meet bugs or faults that need a reset to fix them.</p></article>
</div>

<div class="abs services">
  <ul>
    <li><svg width="26" height="22" viewBox="0 0 26 22"><rect x="1" y="4" width="15" height="11" fill="#f26b1d"/><path d="M16 8h5l4 4v3h-9z" fill="#f26b1d"/><circle cx="6" cy="18" r="3" fill="#f26b1d"/><circle cx="20" cy="18" r="3" fill="#f26b1d"/></svg><div><b>FREE SHIPPING</b><span>Free shipping provinces to<br>Hanoi &amp; HCM</span></div></li>
    <li><svg width="24" height="24" viewBox="0 0 24 24"><path d="M4 12a8 8 0 0 1 14-5M20 12a8 8 0 0 1-14 5" fill="none" stroke="#f26b1d" stroke-width="3"/><path d="M19 2v6h-6zM5 22v-6h6z" fill="#f26b1d"/></svg><div><b>CHANGE PAY WITHIN 24 HOURS</b><span>Change quickly return the product<br>within 24 hours of the stock</span></div></li>
    <li><svg width="22" height="24" viewBox="0 0 22 24"><path d="M11 1l9 4v7c0 6-4 9-9 11-5-2-9-5-9-11V5z" fill="#f26b1d"/><path d="M7 12l3 3 5-6" fill="none" stroke="#fff" stroke-width="2"/></svg><div><b>CREDITS TOP</b><span>Products authorized by the<br>manufacturer</span></div></li>
    <li><svg width="24" height="24" viewBox="0 0 24 24"><path d="M4 14a8 8 0 0 1 16 0" fill="none" stroke="#f26b1d" stroke-width="3"/><rect x="2" y="13" width="5" height="8" rx="2" fill="#f26b1d"/><rect x="17" y="13" width="5" height="8" rx="2" fill="#f26b1d"/></svg><div><b>24/7 FREE CONSULTATION</b><span>Hotline: <b style="display:inline;color:#e21b1b">0907 12 34 56</b></span></div></li>
  </ul>
</div>

<footer class="abs footer">
  <section><h5>Company information</h5><ul><li>Company information</li><li>About the company</li><li>Systems supermarkets</li><li>Recruitment</li></ul></section>
  <section><h5>Customer support</h5><ul><li>Contact and suggestions</li><li>Shopping Guide Online</li><li>Installment buying guide</li><li>Regulates operations management</li></ul></section>
  <section><h5>Purchase policy</h5><ul><li>Regulations and policies</li><li>Warranty policy - change pay</li><li>Membership Policy</li><li>Delivery and installation</li></ul></section>
  <section class="contact"><h5>Contact us</h5><ul><li><i></i><span>Address: 4th Floor, Harbor Group 442 Kestrel Street, Bay District, Lakeview</span></li><li><i></i><span>Hotline 1: (84) 6674 5332</span></li></ul></section>
</footer>

<div class="abs bottom">© Copyright <b>GIZMINIBOX</b></div>

</body>
</html>
```